Business card with logo and words.

Colours: aqua and white (but open to suggestions).
Double sided card ok.
Need to convey competence, calmness, listening skills
Words:
Quiet Harbour Care Guidance
Ruth Pemberly
RN, RM, MQDNS, Grad Dip Gr & Pall Care Couns, Grad Cert Pall Care in Aged Care
quietharbourcg@mailvane.net

```html
<!DOCTYPE html>
<html lang="en">
<head>
<meta charset="utf-8">
<title>Ruth Pemberly – Business Card</title>
<link rel="stylesheet" href="https://fonts.googleapis.com/css2?family=Ubuntu:wght@400&display=swap">
<style>
  :root {
    --cream: #f5f9dc;
    --aqua: #3cc4c8;
    --aqua-bright: #5ef5f8;
    --teal-deep: #1e7a84;
    --teal-mid: #2a8a92;
    --band-top: #55eef2;
    --ink: #111111;
    --page: #ffffff;
  }
  html, body {
    margin: 0;
    padding: 0;
    width: 1200px;
    height: 687px;
    overflow: hidden;
    background: var(--page);
  }
  .card {
    position: relative;
    width: 1200px;
    height: 687px;
    border-radius: 46px;
    overflow: hidden;
    background: var(--cream);
    font-family: "Ubuntu", sans-serif;
    font-weight: 400;
  }
  .brand {
    position: absolute;
    left: 57px;
    top: 120px;
    width: 300px;
    text-align: center;
    color: var(--aqua);
  }
  .brand-mark {
    display: block;
    width: 34px;
    height: 34px;
    margin: 0 auto 22px;
    border-radius: 50%;
    background: var(--aqua);
  }
  .brand-name {
    font-size: 35px;
    line-height: 1.25;
    margin: 0;
  }
  .credentials {
    position: absolute;
    right: 72px;
    top: 90px;
    text-align: right;
    margin: 0;
    padding: 0;
    list-style: none;
    color: var(--aqua);
    font-size: 47px;
    line-height: 72px;
    white-space: nowrap;
  }
  .email {
    color: var(--ink);
    font-size: 44px;
  }
  .accent-stripe {
    position: absolute;
    left: 0;
    top: 421px;
    width: 100%;
    height: 22px;
    background: linear-gradient(90deg, var(--teal-mid) 0%, var(--aqua-bright) 50%, var(--teal-mid) 100%);
  }
  .name-band {
    position: absolute;
    left: 0;
    top: 464px;
    width: 100%;
    height: 223px;
    background: linear-gradient(180deg, var(--band-top) 0%, var(--aqua) 45%, var(--teal-deep) 100%);
    display: flex;
    align-items: center;
    justify-content: center;
  }
  .person-name {
    margin: 0;
    color: var(--cream);
    font-size: 89px;
    font-weight: 400;
    letter-spacing: 1px;
  }
</style>
</head>
<body>
  <div class="card">
    <div class="brand">
      <span class="brand-mark"></span>
      <p class="brand-name">Quiet Harbour<br>Care Guidance</p>
    </div>

    <ul class="credentials">
      <li>RN, RM, MQDNS</li>
      <li>Grad Dip Gr &amp; Pall Care Couns</li>
      <li>Grad Cert Pall Care in Aged Care</li>
      <li class="email">quietharbourcg@mailvane.net</li>
    </ul>

    <div class="accent-stripe"></div>

    <div class="name-band">
      <h1 class="person-name">Ruth Pemberly</h1>
    </div>
  </div>
</body>
</html>
```